Stationary for Wealth Management Firm

We need stationary design based on our new business cards. We would like it to be simple, clean and understated. A lot of our clients are seniors so the fonts cannot be too small. Our colors are dark blue and light grey.

This is what we need:

1. Letterhead US Letter – 8.5" x 11" CMYK 300 DPI
2. Invoice US Letter – 8.5" x 11" CMYK 300 DPI
3. Fax Cover Sheet US Letter – 8.5" x 11" CMYK 300 DPI
4. Email Signature

Including: logo, motto, address with phone and fax numbers, web address, and compliance disclosure.

5. Standard Envelope #10 – 9,5” x 4,125” CMYK 300 Dpi
6. Large Envelope – 9” x 12” CMYK 300 Dpi

Including: logo, motto, addresses without phone and fax numbers, web address, and compliance disclosure.

7. Letterhead Follower US Letter – 8.5" x 11" CMYK 300 DPI

Including: logo, motto, and web address.

8. Flat Invitation Cards – 6” x 4” CMYK 300 Dpi
9. Pocket Folder – 9" x 12”, CMYK 300 Dpi

Including: logo and motto.

Here is the info:

Company: Harrowmere Wealth Management LLC
Address 1: 4715 Lantern Ave. Suite K-12, Maple Hollow, PA, 19021
Phone 1: 1-215-555-0172
Address 2: 618 Fenwick Circle, Elderton Twp., PA, 19365
Phone 2: 1-610-555-0139
Fax: 1-484-555-0196
Motto: Steady Hands Since Day One (in grey #A8A8A8 and US Declaration font)
Web address: www.harrowmerewealth.example
Compliance disclosure: Securities and Advisory Services offered through QVR Capital. Member NASTO/CUDA.
Logo: in uploaded files

Industry/Entity Type

Business

Requirements
Must have
• Need to blend the business card look and feel with the brochure/website look and feel.

```html
<!DOCTYPE html>
<html lang="en">
<head>
<meta charset="utf-8">
<title>Harrowmere Wealth Management – Invoice &amp; Fax Cover</title>
<link rel="stylesheet" href="https://fonts.googleapis.com/css2?family=Cormorant+Garamond:wght@500&family=Arimo:wght@400&family=Pinyon+Script&family=Gelasio:wght@400&family=Carlito&display=swap">
<style>
  :root {
    --backdrop: #e2e2e2;
    --paper: #ffffff;
    --brand-blue: #3d3f58;
    --motto-grey: #a8a8a8;
    --rule-grey: #b9b9b9;
    --band-grey: #d9d9d9;
    --text-grey: #6e6e6e;
    --ink: #222222;
  }
  * { box-sizing: border-box; margin: 0; padding: 0; }
  html, body { width: 1200px; height: 800px; overflow: hidden; }
  body { background: var(--backdrop); position: relative; font-family: "Arimo", Arial, sans-serif; }

  .sheet { position: absolute; top: 111px; width: 412px; height: 574px; background: var(--paper); }
  .sheet--invoice { left: 164px; }
  .sheet--fax { left: 612px; }

  .brand { position: absolute; left: 29px; top: 26px; display: flex; align-items: center; gap: 7px; color: var(--brand-blue); }
  .brand__square { width: 30px; height: 30px; background: var(--brand-blue); }
  .brand__name { font-family: "Cormorant Garamond", Georgia, serif; font-weight: 500; font-size: 15px; letter-spacing: 0.6px; line-height: 1; }
  .brand__sub { font-family: "Arimo", Arial, sans-serif; font-size: 7.5px; letter-spacing: 0.3px; line-height: 1.3; }
  .motto { position: absolute; right: 34px; top: 30px; font-family: "Pinyon Script", cursive; font-size: 15px; color: var(--motto-grey); }

  /* invoice */
  .billing { position: absolute; left: 29px; top: 100px; width: 190px; border: 1px solid var(--rule-grey); font-size: 6.5px; color: var(--text-grey); }
  .billing__row { height: 8.8px; line-height: 8.4px; padding-left: 2px; border-top: 1px solid var(--rule-grey); }
  .billing__row:first-child { border-top: 0; background: var(--band-grey); }
  .invoice-meta { position: absolute; left: 262px; top: 101px; color: var(--text-grey); font-size: 6.5px; }
  .invoice-meta__title { font-size: 10px; color: #555; letter-spacing: 0.3px; margin-bottom: 1px; }
  .invoice-meta__date { margin-top: 10px; }

  .line-items { position: absolute; left: 29px; top: 163px; width: 349px; border-collapse: collapse; font-size: 7px; color: var(--text-grey); }
  .line-items th { background: var(--band-grey); font-weight: 400; height: 19px; border: 1px solid var(--rule-grey); }
  .line-items td { height: 19.4px; border: 1px solid var(--rule-grey); }
  .col-qty { width: 42px; } .col-desc { width: 193px; } .col-unit { width: 57px; } .col-total { width: 57px; }

  .notes { position: absolute; left: 29px; top: 380px; width: 220px; height: 97px; border: 1px solid var(--rule-grey); }
  .notes__head { background: var(--band-grey); height: 20px; line-height: 20px; padding-left: 3px; font-size: 8px; color: var(--text-grey); }

  .amount-due { position: absolute; left: 265px; top: 380px; width: 113px; border: 1px solid var(--rule-grey); font-size: 6.8px; color: var(--text-grey); }
  .amount-due__head { background: var(--band-grey); height: 20px; line-height: 20px; text-align: center; }
  .amount-due__row { display: flex; height: 19.2px; border-top: 1px solid var(--rule-grey); }
  .amount-due__label { width: 57px; text-align: right; padding-right: 3px; line-height: 18px; border-right: 1px solid var(--rule-grey); }
  .amount-due__row--total .amount-due__label { font-size: 8.5px; }

  .footer { position: absolute; left: 29px; top: 518px; font-size: 6px; line-height: 7.6px; color: var(--text-grey); }
  .footer__web { margin-bottom: 2.5px; }
  .footer__office + .footer__office { margin-top: 3px; }
  .disclosure { position: absolute; right: 34px; top: 547px; font-size: 5.5px; line-height: 7px; color: var(--text-grey); }

  /* fax */
  .fax-title { position: absolute; left: 49px; top: 132px; font-family: "Gelasio", Georgia, serif; font-size: 50px; line-height: 1; color: var(--ink); }
  .fax-fields { position: absolute; left: 57px; top: 195px; width: 300px; font-family: "Carlito", Calibri, sans-serif; font-size: 5.6px; color: #333; }
  .fax-fields__row { display: flex; height: 19px; align-items: center; border-bottom: 1px solid #777; }
  .fax-fields__label { width: 27px; }
  .fax-fields__value { width: 124px; }
  .fax-flags { position: absolute; left: 58px; top: 280px; font-family: "Carlito", Calibri, sans-serif; font-size: 5.6px; color: #333; }
  .fax-flag { position: absolute; white-space: nowrap; display: flex; align-items: center; gap: 3px; }
  .fax-flag__box { width: 4.5px; height: 4.5px; border: 0.8px solid #444; }
  .fax-comments { position: absolute; left: 58px; top: 302px; font-family: "Carlito", Calibri, sans-serif; font-size: 5.6px; color: #333; }
</style>
</head>
<body>

<section class="sheet sheet--invoice" aria-label="Invoice">
  <div class="brand">
    <div class="brand__square"></div>
    <div><div class="brand__name">HARROWMERE</div><div class="brand__sub">WEALTH MANAGEMENT</div></div>
  </div>
  <div class="motto">Steady Hands Since Day One</div>

  <div class="billing">
    <div class="billing__row">Billing Address:</div>
    <div class="billing__row">Company:</div>
    <div class="billing__row">Name:</div>
    <div class="billing__row">Address:</div>
    <div class="billing__row">City/State/Zip:</div>
  </div>

  <div class="invoice-meta">
    <div class="invoice-meta__title">INVOICE</div>
    <div>Invoice Number:</div>
    <div class="invoice-meta__date">Invoice Date:</div>
  </div>

  <table class="line-items">
    <thead><tr><th class="col-qty">Quantity</th><th class="col-desc">Description</th><th class="col-unit">Unit price</th><th class="col-total">Total</th></tr></thead>
    <tbody>
      <tr><td></td><td></td><td></td><td></td></tr>
      <tr><td></td><td></td><td></td><td></td></tr>
      <tr><td></td><td></td><td></td><td></td></tr>
      <tr><td></td><td></td><td></td><td></td></tr>
      <tr><td></td><td></td><td></td><td></td></tr>
      <tr><td></td><td></td><td></td><td></td></tr>
      <tr><td></td><td></td><td></td><td></td></tr>
      <tr><td></td><td></td><td></td><td></td></tr>
      <tr><td></td><td></td><td></td><td></td></tr>
    </tbody>
  </table>

  <div class="notes"><div class="notes__head">Notes</div></div>

  <div class="amount-due">
    <div class="amount-due__head">Amount Due</div>
    <div class="amount-due__row"><div class="amount-due__label">Subtotal</div></div>
    <div class="amount-due__row"><div class="amount-due__label">Tax</div></div>
    <div class="amount-due__row"><div class="amount-due__label">Shipping</div></div>
    <div class="amount-due__row amount-due__row--total"><div class="amount-due__label">Total</div></div>
  </div>

  <div class="footer">
    <div class="footer__web">WWW.HARROWMEREWEALTH.EXAMPLE</div>
    <div class="footer__office">4715 Lantern Ave. Suite K-12, Maple Hollow, PA, 19021<br>[P]&nbsp; 1-215-555-0172</div>
    <div class="footer__office">618 Fenwick Circle, Elderton Twp., PA, 19365<br>[P]&nbsp; 1-610-555-0139&nbsp; [F]&nbsp; 1-484-555-0196</div>
  </div>
  <div class="disclosure">Securities and Advisory Services offered through QVR Capital.<br>Member NASTO/CUDA.</div>
</section>

<section class="sheet sheet--fax" aria-label="Fax cover sheet">
  <div class="brand">
    <div class="brand__square"></div>
    <div><div class="brand__name">HARROWMERE</div><div class="brand__sub">WEALTH MANAGEMENT</div></div>
  </div>
  <div class="motto">Steady Hands Since Day One</div>

  <div class="fax-title">fax</div>

  <div class="fax-fields">
    <div class="fax-fields__row"><span class="fax-fields__label">TO:</span><span class="fax-fields__value">[Recipient name]</span><span class="fax-fields__label">FROM:</span><span>[Your name]</span></div>
    <div class="fax-fields__row"><span class="fax-fields__label">FAX:</span><span class="fax-fields__value">[Recipient fax number]</span><span class="fax-fields__label">PAGES:</span><span>[Number of pages]</span></div>
    <div class="fax-fields__row"><span class="fax-fields__label">PHONE:</span><span class="fax-fields__value">[Recipient phone number]</span><span class="fax-fields__label">DATE:</span><span>[Pick the date]</span></div>
    <div class="fax-fields__row"><span class="fax-fields__label">RE:</span><span class="fax-fields__value">[Subject]</span><span class="fax-fields__label">CC:</span><span>[Names]</span></div>
  </div>

  <div class="fax-flags">
    <span class="fax-flag" style="left:0"><span class="fax-flag__box"></span>Urgent</span>
    <span class="fax-flag" style="left:43px"><span class="fax-flag__box"></span>For Review</span>
    <span class="fax-flag" style="left:100px"><span class="fax-flag__box"></span>Please Comment</span>
    <span class="fax-flag" style="left:172px"><span class="fax-flag__box"></span>Please Reply</span>
    <span class="fax-flag" style="left:234px"><span class="fax-flag__box"></span>Please Recycle</span>
  </div>

  <div class="fax-comments">Comments:&nbsp; [Your comments here]</div>

  <div class="footer">
    <div class="footer__web">WWW.HARROWMEREWEALTH.EXAMPLE</div>
    <div class="footer__office">4715 Lantern Ave. Suite K-12, Maple Hollow, PA, 19021<br>[P]&nbsp; 1-215-555-0172</div>
    <div class="footer__office">618 Fenwick Circle, Elderton Twp., PA, 19365<br>[P]&nbsp; 1-610-555-0139&nbsp; [F]&nbsp; 1-484-555-0196</div>
  </div>
  <div class="disclosure">Securities and Advisory Services offered through QVR Capital.<br>Member NASTO/CUDA.</div>
</section>

</body>
</html>
```